Web Design Project

Psychotherapy and Counselling Practice needs a landing page web design.

My business "Harbourlight Consulting" specialises in the treatment of Anxiety and Depression with a holistic approach, endeavouring to unlock the key that holds us to ransom in a life that is imbalanced, frustrating, and ultimately of our own making due to our own perceptions and behaviours.

There is much that impacts us which we cannot change, but we are always in control of how we think, and how we frame our experiences.....learning to challenge those thoughts and behaviours that are destructive and disempowering opens up a world of joyful possibility. Life is about making choices, learn to make wiser and healthier choices.......

Harbourlight Consulting has a client base of individual clients but will seek to expand to offer services to the Corporate world by offering an adjunct to employers for established "Wellness Programs".

Harbourlight Consulting is a highly professional, ethically bound business, with the needs of the client at the forefront of all we do.

Harbourlight Consulting wishes to avoid the usual "jargon driven" psychobabble offered on many counselling web pages. It aims to be stylishly presented, clean in look and with as few "words" as possible and a largely white background (faster loading and more powerful impact of what is stated), those words contained in the webpage should be meaningful, persuasive and have an impact simply at glance. Harbourlight does not want , or expect, those prospective clients in need of support , to be reading through volumes of industry driven cliches.

At this point Harbourlight is just looking for a high quality landing page. However in time this will likely expand to include other sections such as case studies, video content etc.

Target Market(s)

Those in need of emotional support, suffering mental health issues, and those simply wanting to become self aware supported by a mindful therapist.

Industry/Entity Type

Industry

Requirements
Must have
• The design must incorporate the Harbourlight logo and colour schemes found on the attached files.

```html
<!DOCTYPE html>
<html lang="en">
<head>
<meta charset="utf-8">
<title>Harbourlight Consulting</title>
<link rel="stylesheet" href="https://fonts.googleapis.com/css2?family=Open+Sans:wght@300;600;700&display=swap">
<style>
  :root {
    --green: #8cae1c;
    --green-dark: #7e9e14;
    --grey: #9b9b9b;
    --grey-dark: #7a7a7a;
    --band: #737373;
    --badge: #707070;
    --paper: #ffffff;
    --mist: #f6f6f6;
  }
  * { margin: 0; padding: 0; box-sizing: border-box; }
  html, body { width: 1200px; height: 891px; overflow: hidden; background: var(--paper); }
  body { font-family: "Open Sans", Arial, sans-serif; position: relative; color: var(--grey); }

  .stage { position: absolute; left: 0; top: 130px; width: 1200px; height: 690px;
    background: linear-gradient(90deg, var(--mist) 0%, #fbfbfb 55%, #fdfdfd 100%); }

  .badge { position: absolute; left: 10px; top: 11px; width: 134px; height: 130px;
    background: var(--badge); border-radius: 4px; }
  .badge__register { position: absolute; left: 8px; top: 7px; width: 118px; height: 26px;
    border-radius: 13px; background: var(--green); border: 2px solid #e7f0c8;
    color: #fff; font-weight: 700; font-size: 15px; line-height: 22px; text-align: center; }
  .badge__name { position: absolute; left: 0; width: 134px; top: 66px; text-align: center;
    font-weight: 600; font-size: 15px; color: var(--green); }

  .nav { position: absolute; top: 82px; right: 72px; display: flex; gap: 30px; list-style: none; }
  .nav a { color: var(--green-dark); text-decoration: none; font-weight: 600; font-size: 17px; }

  .brand { position: absolute; left: 80px; top: 448px; font-weight: 300; font-size: 64px;
    letter-spacing: 1px; color: var(--green); }

  .quotes { position: absolute; left: 730px; top: 138px; }
  .quote { font-weight: 600; font-size: 22px; line-height: 37px; }
  .quote .lead { color: var(--green); }
  .quote .line { display: block; padding-left: 12px; }
  .quote__by { font-size: 16px; padding-left: 11px; margin-top: 2px; }
  .quote + .quote { margin-top: 40px; }

  .tagline { position: absolute; left: 741px; top: 476px; font-weight: 600; font-size: 21px; }
  .tagline em { font-style: normal; color: var(--green); }

  .contact { position: absolute; left: 741px; top: 544px; font-weight: 600; }
  .contact__name { font-size: 21px; color: var(--grey-dark); }
  .contact__creds { font-size: 15px; margin-top: 6px; }
  .contact__lines { font-size: 16px; margin-top: 30px; line-height: 26px; }

  .waves { position: absolute; left: 0; top: 0; }

  .footer__copy { position: absolute; left: 83px; top: 850px; font-size: 12px; font-weight: 600; color: var(--grey-dark); }
  .social { position: absolute; left: 432px; top: 835px; display: flex; gap: 11px; }
  .social span { width: 30px; height: 28px; background: var(--green); display: block; }
  .footer__site { position: absolute; right: 72px; top: 846px; font-size: 17px; font-weight: 600; color: var(--grey-dark); }
  .footer__site em { font-style: normal; color: var(--green); }
</style>
</head>
<body>
  <div class="stage"></div>

  <svg class="waves" width="1200" height="891" viewBox="0 0 1200 891" aria-hidden="true">
    <path d="M0 768 Q 500 735 1200 722 L1200 812 L0 812 Z" fill="var(--band)"/>
    <path d="M0 706 Q 520 742 1085 710 Q 560 752 0 742 Z" fill="var(--green)"/>
  </svg>

  <div class="badge">
    <div class="badge__register">Register now</div>
    <div class="badge__name">Harbourlight</div>
  </div>

  <ul class="nav">
    <li><a href="#">HOME</a></li>
    <li><a href="#">ABOUT US</a></li>
    <li><a href="#">CASE STUDIES</a></li>
    <li><a href="#">VIDEO CONTENT</a></li>
  </ul>

  <div class="brand">HARBOURLIGHT</div>

  <div class="quotes">
    <p class="quote"><span class="lead">“Change the law of life.</span>
      <span class="line">And those who look only to the past</span>
      <span class="line">or present are to miss the future.”</span></p>
    <p class="quote__by">( Thomas Avery )</p>
    <p class="quote" style="margin-top:40px">“With the new day comes
      <span class="line">new strength new thoughts.”</span></p>
    <p class="quote__by">( Helen Marsh )</p>
  </div>

  <p class="tagline"><em>Consulting</em> is highly Professional</p>

  <div class="contact">
    <p class="contact__name">MARA ELLISON</p>
    <p class="contact__creds">BA (Psych) BSc (Hons) Psych MBPS</p>
    <p class="contact__lines">Mobile: 0491 570 238<br>E-mail: mara.ellison@harbourmail.net</p>
  </div>

  <p class="footer__copy">© Copyright Harbourlight 2013 . Alright reserve</p>
  <div class="social"><span></span><span></span></div>
  <p class="footer__site">www.<em>harbourlightconsulting</em>.com.au</p>
</body>
</html>
```